ORVALIS MED -DIAGNOSTIC CENTRE FOR IMAGES

Our Activity provides diagnostic services for images (RMI, Tac, RX, Ultrasound etc.)
We would like to create a broschure that illustrates our services.
We would like to give maximum attention to the Diagnostic service dedicated to "HEART", therefore maximum evidence to the world of Cardiology.
In the background we would like to highlight the other diagnostic services dedicated to the Rest of the Body (Brain, Knees Legs etc.)
Target Market(s)
PERSONS WHO NEED TO PERFORM DIAGNOSTIC TESTS (MRI, CT, ULTRASOUND, RX ETC.)
Industry/Entity Type
HEALTH
Requirements
Must have
- The company logo, must have diagnostic images (MRI, CT, X-ray, ultrasound), must be simple and intuitive, which is harmonious with the colors of our company logo
Should not have
- Colours that are not in harmony with our company logo

```html
<!DOCTYPE html>
<html lang="en">
<head>
<meta charset="utf-8">
<title>Orvalis Med – Diagnostic Brochure</title>
<link href="https://fonts.googleapis.com/css2?family=Poppins:wght@400;500;600;700;800&display=swap" rel="stylesheet">
<style>
  :root {
    --stage: #0b4ea2;
    --brand-blue: #1656b8;
    --brand-teal: #139e86;
    --paper: #f7f8fa;
    --ink-soft: #3a6fb8;
    --white: #ffffff;
  }
  * { box-sizing: border-box; margin: 0; padding: 0; }
  html, body { width: 1200px; height: 900px; overflow: hidden; }
  body {
    background: var(--stage);
    font-family: "Poppins", sans-serif;
    position: relative;
  }
  .brochure {
    position: absolute;
    left: 300px; top: 24px;
    width: 600px; height: 852px;
    background: var(--paper);
    overflow: hidden;
  }
  .heart-visual {
    position: absolute; left: 0; top: 0;
    width: 330px; height: 330px;
    background: radial-gradient(circle at 45% 55%, rgba(19,158,134,.35), rgba(22,86,184,.12) 55%, rgba(247,248,250,0) 75%);
  }
  .brand {
    position: absolute; right: 40px; top: 48px;
    text-align: right;
  }
  .brand-name {
    display: inline-flex; align-items: center; gap: 10px;
    font-weight: 700; font-size: 34px; letter-spacing: 1px;
    color: var(--brand-blue); line-height: 1;
  }
  .brand-dot {
    width: 14px; height: 14px; border-radius: 50%;
    background: var(--brand-teal);
  }
  .brand-tagline {
    font-size: 13px; font-weight: 500; color: var(--brand-teal);
    margin-top: 6px;
  }
  .headline {
    position: absolute; right: 40px; top: 140px;
    text-align: right;
    font-weight: 800; font-size: 40px; line-height: 1.08;
    color: var(--brand-blue);
  }
  .subhead {
    position: absolute; right: 40px; top: 278px;
    width: 282px; text-align: right;
    font-weight: 600; font-size: 19px; line-height: 1.25;
    color: var(--brand-teal);
    border-top: 3px solid var(--brand-teal);
    border-bottom: 3px solid var(--brand-teal);
    padding: 6px 0;
  }
  .photo-row {
    position: absolute; right: 40px; top: 350px;
    display: flex; gap: 6px;
  }
  .photo {
    width: 90px; height: 78px;
    background: linear-gradient(135deg, #c9d8e8, #6f95bf 60%, #2e5f98);
    border-top: 4px solid var(--brand-blue);
  }
  .services {
    position: absolute; left: 36px; top: 340px;
    width: 234px;
    font-size: 11.5px; line-height: 1.4;
  }
  .section-label {
    display: inline-block;
    background: var(--brand-blue); color: var(--white);
    font-weight: 700; font-size: 12px; letter-spacing: .2px;
    padding: 4px 9px; margin-bottom: 6px;
    white-space: nowrap;
  }
  .section-intro { color: var(--brand-teal); margin-bottom: 4px; }
  .service-list { list-style: none; color: var(--ink-soft); margin-bottom: 16px; }
  .service-list li { margin-bottom: 3px; }
  .scanner-visual {
    position: absolute; right: 20px; top: 450px;
    width: 280px; height: 250px;
    border-radius: 40% 30% 20% 30%;
    background: linear-gradient(160deg, #ffffff, #e3e7ec 55%, #b9c2cc);
    z-index: 2;
  }
  .footer-wave { position: absolute; left: 0; bottom: 0; width: 600px; height: 230px; }
  .footer {
    position: absolute; left: 0; bottom: 0; width: 600px; height: 130px;
    padding: 0 30px 34px;
    display: flex; align-items: flex-end; justify-content: space-between;
    color: var(--white); z-index: 3;
  }
  .phone { display: flex; align-items: center; gap: 8px; font-weight: 700; font-size: 26px; }
  .contact-list { list-style: none; font-size: 10.5px; line-height: 1.7; }
  .contact-list li { display: flex; align-items: center; gap: 6px; }
  .icon { width: 14px; height: 14px; flex: none; }
</style>
</head>
<body>
  <article class="brochure">
    <div class="heart-visual" role="img" aria-label="Teal and blue wireframe network illustration of a human heart"></div>

    <header class="brand">
      <div class="brand-name"><span class="brand-dot"></span>ORVALIS MED</div>
      <div class="brand-tagline">Health Care Diagnostic</div>
    </header>

    <h1 class="headline">Your Partner in<br>Diagnostic<br>Excellence</h1>
    <p class="subhead">Leading the Way in<br>Cardiology and Beyond</p>

    <div class="photo-row">
      <div class="photo" role="img" aria-label="Clinician performing an ultrasound exam"></div>
      <div class="photo" role="img" aria-label="Medical staff attending a patient"></div>
      <div class="photo" role="img" aria-label="Doctor reviewing an X-ray image"></div>
    </div>

    <section class="services">
      <h2 class="section-label">CARDIOLOGY DIAGNOSTICS</h2>
      <p class="section-intro">At Orvalis Med Diagnostics, we specialize in the diagnosis and treatment of heart conditions.</p>
      <ul class="service-list">
        <li>Electrocardiography (ECG)</li>
        <li>Echocardiography</li>
        <li>Stress Tests</li>
        <li>Cardiac MRI</li>
      </ul>
      <h2 class="section-label">OTHER DIAGNOSTIC SERVICES</h2>
      <p class="section-intro">In addition to cardiology, we offer a wide range of diagnostic services for various parts of the body, including:</p>
      <ul class="service-list">
        <li>Brain Imaging: Accurate scans for neurological conditions.</li>
        <li>Musculoskeletal Imaging: Pinpointing issues in your joints and muscles.</li>
      </ul>
    </section>

    <div class="scanner-visual" role="img" aria-label="White CT scanner with patient table"></div>

    <svg class="footer-wave" viewBox="0 0 600 230" preserveAspectRatio="none" aria-hidden="true">
      <path d="M0 70 C 180 70 420 40 600 0 L600 230 L0 230 Z" fill="var(--brand-blue)"/>
      <path d="M0 92 C 200 92 420 60 600 24 L600 230 L0 230 Z" fill="var(--brand-teal)"/>
    </svg>

    <footer class="footer">
      <div class="phone">
        <svg class="icon" style="width:22px;height:22px" viewBox="0 0 24 24" fill="none" stroke="#fff" stroke-width="2.2"><path d="M5 3h4l2 5-3 2a12 12 0 0 0 6 6l2-3 5 2v4a2 2 0 0 1-2 2A18 18 0 0 1 3 5a2 2 0 0 1 2-2z"/></svg>
        (555) 010-4420
      </div>
      <ul class="contact-list">
        <li><svg class="icon" viewBox="0 0 24 24" fill="none" stroke="#fff" stroke-width="2"><circle cx="12" cy="12" r="9"/><path d="M3 12h18M12 3c3 3 3 15 0 18M12 3c-3 3-3 15 0 18"/></svg>OrvalisMedCare.com</li>
        <li><svg class="icon" viewBox="0 0 24 24" fill="none" stroke="#fff" stroke-width="2"><rect x="3" y="5" width="18" height="14"/><path d="M3 5l9 8 9-8"/></svg>hello@OrvalisMedCare.com</li>
        <li><svg class="icon" viewBox="0 0 24 24" fill="#fff"><path d="M12 2a7 7 0 0 0-7 7c0 5 7 13 7 13s7-8 7-13a7 7 0 0 0-7-7zm0 9.5A2.5 2.5 0 1 1 12 6.5a2.5 2.5 0 0 1 0 5z"/></svg>48 Harbor Lane, City, State, Zip</li>
      </ul>
    </footer>
  </article>
</body>
</html>
```